Business Card and Letterhead Design Project

I am starting my own building design business in Melbourne. The business will use my experience to help people make balanced life choices for building and renovating. My target audience is women -particularly mothers. I aim to be approachable and economical. I would like to see a design that uses greens or blues - natural colours. A lot of my work balances design and construction management so design should be flexible.

I want a double sided business card design and a letterhead design that I can use on all office correspondance

Design should have a clean crisp feel - a bit edgey in a feminine way.

Target Market(s)

Potential clients.

Industry/Entity Type

Construction

Requirements
Must have
• Harbourline Design Studio
Rosalind Tebbutt B.Arch

0498 273 461
rosalind@harbourlinedesignstudio.com.au

14 Quandong Street
Elmvale VIC 3188
harbourlinedesignstudio.com.au
Nice to have
• Should have a calming feel to make me seem approachable but still professional.
Should not have
• No photos on the card or building plans.

```html
<!DOCTYPE html>
<html lang="en">
<head>
<meta charset="utf-8">
<title>Harbourline Design Studio — Business Card</title>
<link rel="stylesheet" href="https://fonts.googleapis.com/css2?family=Cinzel:wght@400;600&family=Questrial&display=swap">
<style>
  :root {
    --backdrop: #2a2c2e;
    --card-white: #fbfbfa;
    --teal: #0f7b99;
    --teal-deep: #0a6a86;
    --slate: #4a4d50;
    --band-grey: #8c8f92;
    --text-dark: #3a3c3e;
    --white: #ffffff;
  }
  * { box-sizing: border-box; margin: 0; padding: 0; }
  html, body {
    width: 1200px; height: 800px; overflow: hidden;
    background: var(--backdrop);
  }
  .sheet {
    width: 1200px; height: 800px;
    display: flex; align-items: center; justify-content: center; gap: 44px;
  }
  .card {
    position: relative;
    width: 530px; height: 303px;
    overflow: hidden;
    box-shadow: 0 10px 28px rgba(0,0,0,.45);
  }

  /* Front */
  .card-front { background: var(--card-white); }
  .wordmark {
    position: absolute; text-align: right;
    font-family: "Cinzel", serif; font-weight: 400;
  }
  .card-front .wordmark { top: 34px; right: 34px; color: var(--slate); }
  .wordmark-name { display: block; font-size: 34px; letter-spacing: 1px; line-height: 1; }
  .wordmark-sub { display: block; font-size: 18px; letter-spacing: .5px; margin-top: 4px; }

  .holder {
    position: absolute; left: 38px; top: 164px;
    font-family: "Cinzel", serif; font-weight: 600;
    font-size: 22px; color: var(--teal); letter-spacing: .5px;
  }
  .contact-list {
    position: absolute; left: 38px; top: 204px; list-style: none;
    font-family: "Questrial", sans-serif; font-size: 14px; color: var(--text-dark);
    line-height: 20px;
  }
  .contact-label { color: var(--teal); font-weight: 700; margin-right: 5px; }
  .address {
    position: absolute; right: 34px; top: 164px; text-align: right;
    font-family: "Questrial", sans-serif; font-style: normal;
    font-size: 14px; color: var(--text-dark); line-height: 20px;
  }
  .base-band { position: absolute; left: 0; right: 0; bottom: 0; height: 16px; display: flex; }
  .base-band-grey { flex: 0 0 60%; background: var(--band-grey); }
  .base-band-teal { flex: 1; background: var(--teal); }

  /* Back */
  .card-back { background: linear-gradient(160deg, var(--teal) 0%, var(--teal-deep) 100%); }
  .card-back .wordmark { top: 92px; left: 0; right: 0; text-align: center; color: var(--white); }
  .card-back .wordmark-name { font-size: 40px; }
  .card-back .wordmark-sub { font-size: 21px; }
  .back-curve { position: absolute; left: 0; bottom: 0; width: 530px; height: 110px; }
  .back-curve-fill { fill: var(--band-grey); }
  .back-curve-edge { fill: none; stroke: var(--white); stroke-width: 4; }
</style>
</head>
<body>
<main class="sheet">
  <section class="card card-front" aria-label="Business card front">
    <div class="wordmark">
      <span class="wordmark-name">Harbourline</span>
      <span class="wordmark-sub">Design Studio</span>
    </div>
    <h1 class="holder">ROSALIND TEBBUTT</h1>
    <ul class="contact-list">
      <li><span class="contact-label">T:</span>0498 273 461</li>
      <li><span class="contact-label">E:</span>rosalind@harbourlinedesignstudio.com.au</li>
      <li><span class="contact-label">W:</span>www.harbourlinedesignstudio.com.au</li>
    </ul>
    <address class="address">14 Quandong Street<br>Elmvale VIC 3188</address>
    <div class="base-band"><span class="base-band-grey"></span><span class="base-band-teal"></span></div>
  </section>

  <section class="card card-back" aria-label="Business card back">
    <div class="wordmark">
      <span class="wordmark-name">Harbourline</span>
      <span class="wordmark-sub">Design Studio</span>
    </div>
    <svg class="back-curve" viewBox="0 0 530 110" aria-hidden="true">
      <path class="back-curve-fill" d="M0 80 Q265 30 530 0 L530 110 L0 110 Z"/>
      <path class="back-curve-edge" d="M0 80 Q265 30 530 0"/>
    </svg>
  </section>
</main>
</body>
</html>
```